Text only wordpress site to capture emails

Refer to inspiration upload for list of sites that will be useful for you.

We need a site that will be used to capture emails from clients that follow us on social media. The site will be all text, pretty simple. I have a couple of text sites that I like and we can use them for an example.

Menu section will have home, archive, about.
Footer will have © and Website Privacy Policy | Legal and Policies
There will be some text on the home page and an email capture.

This site will be all text no pictures.

I discuss office politics so the text portions will have some questions and answers on this and then prompt for the visitor to subscribe to my email list.

The only purpose of the site is to build an email list from existing social media followers so the site will be pretty simple in and of itself.

• Text only, similar Q&A to uploaded pics.

I will use a template from letter pinecone dotcom for email capture.

I like the simple couriernew font family that is on both sites supplied in the uploads.
• If you use any color it needs to be very minimal.

```html
<!DOCTYPE html>
<html lang="en">
<head>
<meta charset="UTF-8">
<title>Company Logo — Office Politics Q&amp;A</title>
<link href="https://fonts.googleapis.com/css2?family=Courier+Prime:wght@400;700&family=Roboto:wght@300;400;500;700&display=swap" rel="stylesheet">
<style>
:root{
  --ink:#2f343d;
  --ink-soft:#6b7079;
  --muted:#9a9ea6;
  --line:#e4e5e9;
  --header:#4b505a;
  --hero:#f6f6fb;
  --band:#f4f4f6;
  --white:#ffffff;
  --btn:#454b56;
  --btn-light:#c9cbd0;
  --mono:"Courier Prime", "Courier New", monospace;
  --sans:"Roboto", Arial, sans-serif;
}
*{box-sizing:border-box;margin:0;padding:0}
html,body{width:1200px;height:3272px;overflow:hidden}
body{background:var(--white);color:var(--ink);font-family:var(--mono)}
.wrap{width:896px;margin:0 auto}

/* header */
.site-header{height:92px;background:var(--header)}
.site-header .wrap{width:930px;height:92px;display:flex;align-items:center;justify-content:space-between}
.brand{font-family:var(--sans);font-weight:500;font-size:22px;color:var(--white);letter-spacing:.5px}
.nav{display:flex;gap:14px;font-family:var(--sans);font-size:15px}
.nav a{color:var(--white);text-decoration:none;padding:10px 22px;border-radius:2px}
.nav a.active{background:var(--white);color:var(--ink)}

/* hero */
.hero{height:568px;background:var(--hero);text-align:center;padding-top:110px}
.hero h1{font-family:var(--sans);font-weight:300;font-size:40px;line-height:52px;color:var(--ink)}
.hero h1 strong{font-weight:500}
.hero p{margin:22px auto 0;width:620px;font-size:15px;line-height:24px;color:var(--ink-soft)}
.signup{margin:44px auto 0;width:500px;height:60px;background:var(--white);display:flex;align-items:center;justify-content:space-between;padding:0 10px 0 24px;box-shadow:0 6px 20px rgba(40,45,60,.08)}
.signup span{font-family:var(--sans);font-size:14px;color:var(--muted)}
.btn{display:inline-block;background:var(--btn);color:var(--white);font-family:var(--sans);font-size:14px;padding:12px 18px;border-radius:2px}

/* faq */
.faq{padding-top:60px;height:1428px}
.faq h2{font-family:var(--sans);font-weight:500;font-size:26px;color:var(--ink);margin-bottom:30px}
.faq-item{height:172px;padding-top:38px;border-bottom:1px solid var(--line)}
.faq-item:first-of-type{padding-top:6px;height:140px}
.faq-q{font-weight:700;font-size:16px;margin-bottom:20px}
.faq-a{display:flex;gap:10px;font-size:13px;line-height:20px;color:var(--ink-soft)}
.faq-a b{color:var(--ink)}

/* blog */
.blog{background:var(--band);height:912px;padding-top:72px}
.blog-head{display:flex;justify-content:space-between;align-items:center}
.blog-head h2{font-family:var(--sans);font-weight:300;font-size:34px}
.blog-head h2 strong{font-weight:500}
.search{width:240px;height:40px;background:var(--white);border:1px solid var(--line);font-family:var(--sans);font-size:13px;color:var(--muted);padding:0 14px;display:flex;align-items:center;justify-content:space-between}
.cards{margin-top:60px;display:grid;grid-template-columns:repeat(3,268px);gap:46px 46px;justify-content:space-between}
.card{position:relative;height:282px;background:var(--white);padding:26px 22px;border:1px solid var(--line)}
.card.featured{box-shadow:0 12px 30px rgba(40,45,60,.14);border-color:transparent}
.card-tag{font-size:11px;color:var(--muted);letter-spacing:1px}
.card h3{margin-top:8px;font-size:19px;line-height:24px;font-weight:700}
.card p{margin-top:14px;font-size:12px;line-height:17px;color:var(--ink-soft)}
.card-go{position:absolute;right:16px;bottom:16px;width:26px;height:26px;background:var(--btn-light);display:flex;align-items:center;justify-content:center}
.card.featured .card-go{background:var(--btn)}
.more{display:block;width:96px;margin:60px auto 0;text-align:center}

/* footer */
.site-footer{height:272px;padding-top:70px}
.footer-signup{width:480px;height:56px;margin:0 auto;border:1px solid var(--line);display:flex;align-items:center;justify-content:space-between;padding:0 8px 0 20px}
.footer-signup span{font-family:var(--sans);font-size:14px;color:var(--muted)}
.footer-nav{position:relative;margin-top:30px;display:flex;justify-content:center;gap:40px;font-family:var(--sans);font-size:15px}
.footer-nav a{color:var(--ink);text-decoration:none}
.social{position:absolute;right:0;top:0;display:flex;gap:12px}
.social i{width:14px;height:14px;border-radius:50%;background:var(--ink);display:block}
.legal{margin-top:22px;border-top:1px solid var(--line);padding-top:22px;display:flex;justify-content:space-between;font-family:var(--sans);font-size:13px;color:var(--ink-soft)}
.legal a{color:var(--ink-soft);text-decoration:underline}
</style>
</head>
<body>
<header class="site-header">
  <div class="wrap">
    <div class="brand">COMPANY LOGO</div>
    <nav class="nav"><a class="active" href="#">Home</a><a href="#">Archive</a><a href="#">About</a></nav>
  </div>
</header>

<section class="hero">
  <h1>Lorem Ipsum is <strong>Simply Dummy<br>Text of the Printing</strong></h1>
  <p>Lorem Ipsum is simply dummy text of the printing and typesetting industry. Lorem Ipsum has been the industry's.</p>
  <div class="signup"><span>Your Email Address</span><span class="btn">Subscribe</span></div>
</section>

<section class="faq wrap">
  <h2>Frequently Asked Questions</h2>
  <div class="faq-item"><div class="faq-q">Q: Lorem Ipsum is simply dummy text ?</div><div class="faq-a"><b>A:</b><span>Lorem Ipsum is simply dummy text of the printing and typesetting industry. Lorem Ipsum has been the industry's standard dummy text ever since the 1500s, when an unknown printer took a galley of type and scrambled it to make a type specimen book. It has survived not only five centuries</span></div></div>
  <div class="faq-item"><div class="faq-q">Q: Lorem Ipsum is simply dummy text ?</div><div class="faq-a"><b>A:</b><span>Lorem Ipsum is simply dummy text of the printing and typesetting industry. Lorem Ipsum has been the industry's standard dummy text ever since the 1500s, when an unknown printer took a galley of type and scrambled it to make a type specimen book. It has survived not only five centuries</span></div></div>
  <div class="faq-item"><div class="faq-q">Q: Lorem Ipsum is simply dummy text ?</div><div class="faq-a"><b>A:</b><span>Lorem Ipsum is simply dummy text of the printing and typesetting industry. Lorem Ipsum has been the industry's standard dummy text ever since the 1500s, when an unknown printer took a galley of type and scrambled it to make a type specimen book. It has survived not only five centuries</span></div></div>
  <div class="faq-item"><div class="faq-q">Q: Lorem Ipsum is simply dummy text ?</div><div class="faq-a"><b>A:</b><span>Lorem Ipsum is simply dummy text of the printing and typesetting industry. Lorem Ipsum has been the industry's standard dummy text ever since the 1500s, when an unknown printer took a galley of type and scrambled it to make a type specimen book. It has survived not only five centuries</span></div></div>
  <div class="faq-item"><div class="faq-q">Q: Lorem Ipsum is simply dummy text ?</div><div class="faq-a"><b>A:</b><span>Lorem Ipsum is simply dummy text of the printing and typesetting industry. Lorem Ipsum has been the industry's standard dummy text ever since the 1500s, when an unknown printer took a galley of type and scrambled it to make a type specimen book. It has survived not only five centuries</span></div></div>
  <div class="faq-item"><div class="faq-q">Q: Lorem Ipsum is simply dummy text ?</div><div class="faq-a"><b>A:</b><span>Lorem Ipsum is simply dummy text of the printing and typesetting industry. Lorem Ipsum has been the industry's standard dummy text ever since the 1500s, when an unknown printer took a galley of type and scrambled it to make a type specimen book. It has survived not only five centuries</span></div></div>
  <div class="faq-item"><div class="faq-q">Q: Lorem Ipsum is simply dummy text ?</div><div class="faq-a"><b>A:</b><span>Lorem Ipsum is simply dummy text of the printing and typesetting industry. Lorem Ipsum has been the industry's standard dummy text ever since the 1500s, when an unknown printer took a galley of type and scrambled it to make a type specimen book. It has survived not only five centuries</span></div></div>
</section>

<section class="blog">
  <div class="wrap">
    <div class="blog-head">
      <h2>Latest <strong>Blog</strong></h2>
      <div class="search"><span>Search</span><svg width="10" height="6" viewBox="0 0 10 6"><path d="M1 1l4 4 4-4" fill="none" stroke="#9a9ea6" stroke-width="1.4"/></svg></div>
    </div>
    <div class="cards">
      <article class="card"><div class="card-tag">BLOG</div><h3>Lorem Ipsum is simply dummy text of the</h3><p>Lorem Ipsum is simply dummy text of the printing and typesetting industry. Lorem Ipsum has been the industry's standard dummy text ever since the 1500s.</p><span class="card-go"><svg width="10" height="10" viewBox="0 0 10 10"><path d="M1 5h7M5 2l3 3-3 3" fill="none" stroke="#fff" stroke-width="1.4"/></svg></span></article>
      <article class="card featured"><div class="card-tag">BLOG</div><h3>Lorem Ipsum is simply dummy text of the</h3><p>Lorem Ipsum is simply dummy text of the printing and typesetting industry. Lorem Ipsum has been the industry's standard dummy text ever since the 1500s.</p><span class="card-go"><svg width="10" height="10" viewBox="0 0 10 10"><path d="M1 5h7M5 2l3 3-3 3" fill="none" stroke="#fff" stroke-width="1.4"/></svg></span></article>
      <article class="card"><div class="card-tag">BLOG</div><h3>Lorem Ipsum is simply dummy text of the</h3><p>Lorem Ipsum is simply dummy text of the printing and typesetting industry. Lorem Ipsum has been the industry's standard dummy text ever since the 1500s.</p><span class="card-go"><svg width="10" height="10" viewBox="0 0 10 10"><path d="M1 5h7M5 2l3 3-3 3" fill="none" stroke="#fff" stroke-width="1.4"/></svg></span></article>
      <article class="card"><div class="card-tag">BLOG</div><h3>Lorem Ipsum is simply dummy text of the</h3><p>Lorem Ipsum is simply dummy text of the printing and typesetting industry. Lorem Ipsum has been the industry's standard dummy text ever since the 1500s.</p><span class="card-go"><svg width="10" height="10" viewBox="0 0 10 10"><path d="M1 5h7M5 2l3 3-3 3" fill="none" stroke="#fff" stroke-width="1.4"/></svg></span></article>
      <article class="card"><div class="card-tag">BLOG</div><h3>Lorem Ipsum is simply dummy text of the</h3><p>Lorem Ipsum is simply dummy text of the printing and typesetting industry. Lorem Ipsum has been the industry's standard dummy text ever since the 1500s.</p><span class="card-go"><svg width="10" height="10" viewBox="0 0 10 10"><path d="M1 5h7M5 2l3 3-3 3" fill="none" stroke="#fff" stroke-width="1.4"/></svg></span></article>
      <article class="card"><div class="card-tag">BLOG</div><h3>Lorem Ipsum is simply dummy text of the</h3><p>Lorem Ipsum is simply dummy text of the printing and typesetting industry. Lorem Ipsum has been the industry's standard dummy text ever since the 1500s.</p><span class="card-go"><svg width="10" height="10" viewBox="0 0 10 10"><path d="M1 5h7M5 2l3 3-3 3" fill="none" stroke="#fff" stroke-width="1.4"/></svg></span></article>
    </div>
    <span class="btn more">More</span>
  </div>
</section>

<footer class="site-footer">
  <div class="footer-signup"><span>Your Email Address</span><span class="btn">Subscribe</span></div>
  <div class="wrap">
    <nav class="footer-nav"><a href="#">Home</a><a href="#">Archive</a><a href="#">About</a>
      <div class="social" aria-label="Social links"><i></i><i></i><i></i></div>
    </nav>
    <div class="legal"><span>Copyright 2021 Company Name</span><span><a href="#">Privacy Policy</a> &nbsp;|&nbsp; <a href="#">Legal and Policies</a></span></div>
  </div>
</footer>
</body>
</html>
```